Business Card Design

Velvet Pixel Promotions

An online marketing consulting & strategy business for the cosmetic niche

We specialise in Increasing Leads, Conversions & Content Marketing

I am looking for a very clean, BOLD business card that is simple & effective

Target Market(s)

cosmetic surgeons & cosmetic clinics

Industry/Entity Type

Marketing

Contact Information for Business Card

Darren Okoye
Online Marketing Strategist

Darren@VelvetPixelPromotions.example
0491 268 517

LinkedIn: in/darrenokoye

```html
<!DOCTYPE html>
<html lang="en">
<head>
<meta charset="utf-8">
<title>Velvet Pixel Promotions – Business Card</title>
<link rel="stylesheet" href="https://fonts.googleapis.com/css2?family=Mulish:wght@500;700;800&display=swap">
<style>
  :root {
    --backdrop: #2a2a2a;
    --card: #ffffff;
    --ink: #111111;
    --block: #141414;
    --brand-grey: #7a7a7a;
    --brand-teal: #2aa9c4;
    --mark-muted: #4b6e6a;
  }
  * { margin: 0; padding: 0; box-sizing: border-box; }
  html, body {
    width: 1200px; height: 900px; overflow: hidden;
    background: var(--backdrop);
    font-family: "Mulish", sans-serif;
  }
  .card {
    position: absolute;
    width: 640px; height: 365px;
    background: var(--card);
    overflow: hidden;
    box-shadow: 0 10px 30px rgba(0,0,0,.45);
  }
  .card--front { left: 80px; top: 50px; }
  .card--back  { left: 480px; top: 485px; }

  .block {
    position: absolute; right: 0;
    background: var(--block);
  }
  .card--front .block { top: 0; width: 200px; height: 150px; }
  .card--back .block {
    top: 50px; width: 200px; height: 200px;
    display: flex; flex-direction: column; align-items: center; justify-content: center; gap: 12px;
  }

  .brand {
    position: absolute; left: 40px; bottom: 50px;
    display: flex; align-items: center; gap: 22px;
  }
  .brand__dot {
    width: 84px; height: 84px; border-radius: 50%;
    background: var(--brand-teal);
  }
  .brand__name {
    font-weight: 700; font-size: 32px; line-height: 1.02;
    letter-spacing: 4px; text-transform: uppercase;
    color: var(--brand-grey);
  }

  .block__dot {
    width: 70px; height: 70px; border-radius: 50%;
    border: 8px solid var(--mark-muted);
  }
  .block__name {
    font-weight: 700; font-size: 13px; letter-spacing: 1px;
    text-transform: uppercase; color: var(--mark-muted); text-align: center;
  }

  .contact {
    position: absolute; right: 212px; top: 92px;
    text-align: right; color: var(--ink);
  }
  .contact__name { font-weight: 800; font-size: 34px; line-height: 1; }
  .contact__role { font-weight: 700; font-size: 17px; margin-top: 2px; }
  .contact__line { font-weight: 500; font-size: 14px; margin-top: 6px; display: flex; justify-content: flex-end; align-items: center; gap: 6px; }
  .contact__line:first-of-type { margin-top: 22px; }
  .contact__icon { width: 15px; height: 15px; background: var(--ink); border-radius: 2px; }
  .contact__email { font-weight: 700; font-size: 15px; margin-top: 48px; }
</style>
</head>
<body>
  <section class="card card--front">
    <div class="block"></div>
    <div class="brand">
      <span class="brand__dot"></span>
      <span class="brand__name">Velvet<br>Pixel<br>Promotions</span>
    </div>
  </section>

  <section class="card card--back">
    <div class="contact">
      <p class="contact__name">Darren Okoye</p>
      <p class="contact__role">Online Marketing Strategist</p>
      <p class="contact__line">0491 268 517</p>
      <p class="contact__line"><span class="contact__icon"></span>in/darrenokoye</p>
      <p class="contact__email">Darren@VelvetPixelPromotions.example</p>
    </div>
    <div class="block">
      <span class="block__dot"></span>
      <span class="block__name">Velvet Pixel<br>Promotions</span>
    </div>
  </section>
</body>
</html>
```